Brivane Communications - veteran and exclusive boutique copywriting agency

PROJECT NEEDS:
1. Website design - full homepage design and inner page top banner design
2. Logo design
* Please see attached Briefs (Word Docs) for descriptions of what is needed for 1 and 2 above.
ABOUT THE CLIENT:
Brivane Communications is a veteran and exclusive boutique copywriting agency run by Martin Olafsky. Martin is an award-winning published novelist and an accomplished executive ghostwriter with articles regularly published prominent technology publications like Pulsar, ByteHarbor, CapitalDrift, and more. For nearly three decades, Martin has focused solely on the technology sector - serving clients in Israel, Europe and the US.

Target Market(s)

hi-tech companies run by serious, confident professionals.

Industry/Entity Type

Business

Number of Pages Required

2 page

Font styles to use
Sans Serif
Other font styles liked:
• font should be modern

Colors
0054AA
0677BA
7BADD7
CADEEF
E8F1F8
F0912C
F2A743
F7CA91
FBE8D2
FDF5EE

Requirements
Must have
• psd files for logo, homepage design, and inner page top banner design
Nice to have
• Please see attached Website and Logo Design Briefs (Word Docs)
Should not have

```html
<!DOCTYPE html>
<html lang="en">
<head>
<meta charset="utf-8">
<title>Brivane Communications</title>
<link href="https://fonts.googleapis.com/css2?family=Montserrat:wght@400;500;600;700;800&display=swap" rel="stylesheet">
<style>
:root{
  --blue:#0054AA;
  --orange:#F0912C;
  --orange-soft:#F2A743;
  --dark:#232323;
  --ink:#1c1c1c;
  --text:#333;
  --paper:#f4f2ee;
  --grey:#ececec;
  --white:#fff;
}
*{margin:0;padding:0;box-sizing:border-box}
html,body{width:1200px;height:3661px;overflow:hidden}
body{font-family:'Montserrat',sans-serif;color:var(--text);background:var(--white)}
.page{position:relative;width:1200px;height:3661px;overflow:hidden}
.abs{position:absolute}
.btn{position:absolute;display:flex;align-items:center;justify-content:center;background:var(--blue);color:var(--white);font-weight:700;font-size:13px;letter-spacing:.3px}
.rule{position:absolute;height:3px;width:44px;background:var(--orange)}
h2.section-title{position:absolute;font-weight:800;font-size:31px;color:var(--ink);letter-spacing:.2px}
p.body{position:absolute;font-size:11px;line-height:19px;color:#3a3a3a}

/* hero */
.logo-box{left:31px;top:0;width:133px;height:131px;background:var(--blue);display:flex;align-items:center;justify-content:center;color:var(--white);font-weight:800;font-size:20px;letter-spacing:1px;z-index:3}
.nav{position:absolute;top:31px;left:0;width:1200px;z-index:3}
.nav a{position:absolute;color:var(--white);font-size:10.5px;font-weight:500;text-decoration:none;letter-spacing:.3px}
.nav a.active{font-weight:700}
.nav a.active::after{content:"";position:absolute;left:3px;top:19px;width:24px;height:2px;background:var(--orange)}
.hero-title{left:112px;top:200px;color:var(--white);font-weight:800;line-height:1;z-index:3}
.hero-title span{display:block;font-size:45px;margin-bottom:5px}
.hero-title span.big{font-size:60px;margin-top:6px}
.hero-copy{left:112px;top:380px;color:var(--white);font-size:11px;line-height:15.5px;z-index:3}
.hero-watermark{left:-10px;top:560px;font-size:96px;font-weight:700;color:rgba(255,255,255,.13);white-space:nowrap;letter-spacing:2px;z-index:2}

/* services */
.card{position:absolute;top:803px;width:315px;height:243px;overflow:hidden}
.card .shade{position:absolute;inset:0;background:linear-gradient(180deg,rgba(0,0,0,0) 40%,rgba(0,0,0,.45))}
.card h3{position:absolute;left:18px;color:var(--white);font-weight:700;font-size:17px;letter-spacing:.3px}
.card p{position:absolute;left:20px;top:117px;width:210px;color:var(--white);font-size:11px;line-height:15.5px}
.card .go{position:absolute;bottom:20px;width:24px;height:24px}
.card .icon{position:absolute;left:18px;width:32px;height:32px}

/* can do list */
.service-item{position:absolute;display:flex;align-items:center;font-size:17px;font-weight:500;color:var(--ink)}
.service-item svg{width:48px;height:48px}

/* choose */
.choice{position:absolute;top:3060px;height:233px;width:392px;padding:30px 0 0 44px;overflow:hidden}
.choice h3{font-size:24px;font-weight:800;margin-bottom:10px}
.choice ul{list-style:none}
.choice li{position:relative;padding-left:24px;font-size:11px;line-height:15px;margin-bottom:14px;width:300px}
.choice li::before{content:"";position:absolute;left:2px;top:5px;width:5px;height:5px;border-radius:50%;background:currentColor}

/* footer */
.footer{left:0;top:3341px;width:1200px;height:320px;background:var(--dark)}
.footer h4{position:absolute;top:56px;color:var(--orange);font-size:12px;font-weight:700;letter-spacing:.3px}
.footer ul{position:absolute;top:92px;list-style:none}
.footer li{color:var(--white);font-size:10.5px;font-weight:500;height:25px;display:flex;align-items:center;gap:12px}
.footer li i{display:inline-block;width:8px;height:8px;border-radius:50%;background:var(--white)}
.field{position:absolute;left:972px;width:115px;height:22px;background:var(--white);font-size:9.5px;color:#999;padding:5px 7px}
</style>
</head>
<body>
<div class="page">

<!-- HERO -->
<svg class="abs" style="left:0;top:0" width="1200" height="680" viewBox="0 0 1200 680">
  <defs>
    <linearGradient id="heroPhoto" x1="0" y1="0" x2="1" y2="1">
      <stop offset="0" stop-color="#8b7a64"/>
      <stop offset=".45" stop-color="#6d6357"/>
      <stop offset="1" stop-color="#4a4440"/>
    </linearGradient>
  </defs>
  <g role="img" aria-label="Photo: two children racing soapbox carts down a country road, the front child cheering with a raised fist">
    <polygon points="0,0 1200,0 1200,674 555,674 520,640 0,640" fill="url(#heroPhoto)"/>
  </g>
  <polygon points="200,0 520,0 870,674 555,674 520,640 300,640 540,640 300,200" fill="#F0912C" opacity=".55"/>
  <polygon points="620,0 1200,0 1200,70 870,160" fill="#F0912C" opacity=".55"/>
  <polygon points="1060,0 1200,0 1200,270" fill="#F0912C" opacity=".4"/>
  <polygon points="0,460 0,640 300,640" fill="#F0912C" opacity=".35"/>
</svg>
<div class="abs logo-box">BRIVANE</div>
<nav class="nav">
  <a class="active" style="left:388px">HOME</a>
  <a style="left:465px">ABOUT</a>
  <a style="left:543px">SERVICES</a>
  <a style="left:636px">INDUSTRIES</a>
  <a style="left:739px">PORTFOLIO</a>
  <a style="left:842px">CLIENTS</a>
  <a style="left:926px">CONTACT</a>
</nav>
<h1 class="abs hero-title"><span>THE WORDS THAT</span><span>LAUNCH THE</span><span class="big">CONVERSATION</span></h1>
<p class="abs hero-copy">In a crowded marketspace, your messages need to engage.<br>Your offering needs to rise above the background noise but not by shouting.<br>It’s a conversation, not a speech.</p>
<div class="btn" style="left:112px;top:456px;width:192px;height:45px;z-index:3">LEARN MORE</div>
<div class="abs hero-watermark">BRIVANE COMMUNICATION</div>

<!-- SERVICES -->
<svg class="abs" style="left:0;top:674px" width="1200" height="425"><polygon points="800,0 1200,0 1200,425 1040,425" fill="#f4f4f4"/></svg>
<h2 class="section-title" style="left:0;width:1200px;text-align:center;top:716px">OUR SERVICES</h2>
<div class="rule" style="left:578px;top:763px"></div>

<div class="card" style="left:112px">
  <div class="abs" role="img" aria-label="Photo: boy in a suit shouting into a megaphone" style="inset:0;background:linear-gradient(135deg,#8f8c86,#3c3a38)"></div>
  <div class="shade"></div>
  <svg class="icon" style="top:50px" viewBox="0 0 32 32" fill="none" stroke="#fff" stroke-width="1.5"><rect x="3" y="5" width="20" height="13" rx="2"/><path d="M8 18v5l5-5"/></svg>
  <h3 style="top:84px">MESSAGING</h3>
  <p>IThe Value of a Fresh Perspective Could you be reaching farther? Clearly-defined, accurately-targeted messaging is crucial.</p>
  <svg class="go" style="left:22px" viewBox="0 0 24 24"><circle cx="12" cy="12" r="11" fill="#fff"/><path d="M7 12h9M13 8l4 4-4 4" stroke="#F0912C" stroke-width="2" fill="none"/></svg>
</div>
<div class="card" style="left:442px">
  <div class="abs" role="img" aria-label="Photo: child with goggles and a cardboard rocket pack in front of desert mountains" style="inset:0;background:linear-gradient(180deg,#c9b6a0,#9b7a5f 55%,#6e5a4c)"></div>
  <div class="shade"></div>
  <svg class="icon" style="top:150px" viewBox="0 0 32 32" fill="none" stroke="#fff" stroke-width="1.5"><circle cx="16" cy="12" r="7"/><path d="M10 28l4-8h4l4 8"/></svg>
  <h3 style="top:198px">COLLATERAL &amp; CREATIVE</h3>
  <svg class="go" style="right:14px" viewBox="0 0 24 24"><circle cx="12" cy="12" r="11" fill="none" stroke="#fff" stroke-width="1.5"/><path d="M7 12h9M13 8l4 4-4 4" stroke="#fff" stroke-width="2" fill="none"/></svg>
</div>
<div class="card" style="left:772px">
  <div class="abs" role="img" aria-label="Photo: boy in a suit wearing cardboard wings in a field of grass" style="inset:0;background:linear-gradient(180deg,#e6ddc9,#b8a57c 55%,#6b6142)"></div>
  <div class="shade"></div>
  <svg class="icon" style="top:150px" viewBox="0 0 32 32" fill="none" stroke="#fff" stroke-width="1.5"><rect x="4" y="4" width="24" height="24" rx="2"/><path d="M9 11h14M9 17h14M9 23h8"/></svg>
  <h3 style="top:198px">CONTENT MARKETING</h3>
  <svg class="go" style="right:14px" viewBox="0 0 24 24"><circle cx="12" cy="12" r="11" fill="none" stroke="#fff" stroke-width="1.5"/><path d="M7 12h9M13 8l4 4-4 4" stroke="#fff" stroke-width="2" fill="none"/></svg>
</div>

<!-- ABOUT -->
<div class="abs" style="left:0;top:1099px;width:1200px;height:494px;background:var(--paper)"></div>
<svg class="abs" style="left:0;top:1099px" width="1200" height="494"><polygon points="1200,0 1200,494 782,494" fill="#F0912C"/></svg>
<div class="abs" role="img" aria-label="Portrait photo of Martin Olafsky in a light blue shirt" style="left:751px;top:1157px;width:337px;height:381px;background:radial-gradient(circle at 50% 35%,#3c4d66,#17202f 75%)"></div>
<h2 class="section-title" style="left:185px;top:1199px;font-size:30px">ABOUT MARTIN OLAFSKY</h2>
<div class="rule" style="left:185px;top:1247px"></div>
<p class="body" style="left:185px;top:1287px;width:490px">In nearly two decades in the international marketing trenches, I’ve learned to rapidly define and internalize company messages - and to communicate them at eye-level.</p>
<p class="body" style="left:185px;top:1343px;width:490px">Brivane SmallBorn and raised in the US, I’ve lived and worked in Israel since 1990, and speak fluent Hebrew. I do all client writing myself, so my clients get one-on-one service and a personal guarantee of quality.</p>
<div class="btn" style="left:185px;top:1460px;width:149px;height:39px">LEARN MORE</div>

<!-- VISION -->
<svg class="abs" style="left:0;top:1598px" width="1200" height="624">
  <rect x="0" y="0" width="1200" height="490" fill="#232323"/>
  <g role="img" aria-label="Black and white photo: a young boy in a flat cap shouting into a megaphone">
    <polygon points="0,0 470,0 660,624 0,624" fill="#5d5d5d"/>
  </g>
  <polygon points="410,0 520,0 688,567 578,567" fill="#F0912C"/>
  <polygon points="660,490 1200,490 1200,624 700,624" fill="#fff"/>
</svg>
<h2 class="section-title" style="left:685px;top:1670px;color:#fff;font-size:30px;line-height:37px">GIVING VOICE TO<br>YOUR VISION</h2>
<div class="rule" style="left:685px;top:1759px"></div>
<p class="body" style="left:685px;top:1788px;width:370px;color:#fff">Byline articles in major publications that cement your brand as a thought leader. Engaging blog entries that ensure your company is always part of the conversation. White papers and e-books that inform, educate, entertain and engage.</p>
<p class="body" style="left:685px;top:1882px;width:370px;color:#fff">Content marketing is about sharing your expertise. It’s about showing the world not only what you know, but how well you can explain what you know.</p>
<div class="btn" style="left:685px;top:1975px;width:149px;height:39px">LEARN MORE</div>

<!-- WHAT WE CAN DO -->
<h2 class="section-title" style="left:185px;top:2263px;font-size:30px">WHAT WE CAN DO</h2>
<div class="rule" style="left:185px;top:2311px"></div>
<p class="body" style="left:185px;top:2330px;width:590px">Since 2001, Brivane Communications has had the opportunity to create collateral and content for tens of companies across a wide range of industries. Following is a small selection of recent projects:</p>
<div class="abs" style="left:864px;top:2332px;width:151px;height:40px;border:2px solid #9a9a9a;display:flex;align-items:center;justify-content:center;font-size:12px;font-weight:700;color:#555">VIEW ALL</div>

<div class="service-item" style="left:205px;top:2397px"><svg viewBox="0 0 48 48" fill="none" stroke="#F0912C" stroke-width="1.6"><path d="M4 34l10-6 10 6 16-8M18 8h10v8h-10z"/></svg><span style="margin-left:40px">Contributed Content</span></div>
<div class="service-item" style="left:205px;top:2474px"><svg viewBox="0 0 48 48" fill="none" stroke="#F0912C" stroke-width="1.6"><rect x="8" y="6" width="28" height="36" rx="2"/><path d="M14 16h16M14 24h16M14 32h10"/></svg><span style="margin-left:39px">Blog Content</span></div>
<div class="service-item" style="left:205px;top:2547px"><svg viewBox="0 0 48 48" fill="none" stroke="#F0912C" stroke-width="1.6"><rect x="6" y="6" width="24" height="32" rx="2"/><circle cx="32" cy="32" r="7"/><path d="M37 37l6 6"/></svg><span style="margin-left:40px">Case Studies</span></div>
<div class="service-item" style="left:680px;top:2397px"><svg viewBox="0 0 48 48" fill="none" stroke="#F0912C" stroke-width="1.6"><rect x="4" y="8" width="40" height="26" rx="2"/><path d="M18 42h12M24 34v8"/></svg><span style="margin-left:44px">Web Site Content</span></div>
<div class="service-item" style="left:680px;top:2474px"><svg viewBox="0 0 48 48" fill="none" stroke="#F0912C" stroke-width="1.6"><rect x="6" y="18" width="36" height="24" rx="2"/><path d="M6 18l34-8 2 6M21 24v12l10-6z"/></svg><span style="margin-left:44px">Video - Concept and Script</span></div>
<div class="service-item" style="left:680px;top:2550px"><svg viewBox="0 0 48 48" fill="none" stroke="#F0912C" stroke-width="1.6"><rect x="6" y="8" width="30" height="32" rx="2"/><path d="M12 18h18M12 26h12"/><circle cx="34" cy="34" r="8"/></svg><span style="margin-left:42px">Press Releases</span></div>

<!-- CLIENTS -->
<svg class="abs" style="left:0;top:2623px" width="1200" height="303">
  <rect x="0" y="53" width="1200" height="250" fill="#F0912C"/>
  <polygon points="140,53 308,53 435,303 265,303" fill="#0054AA"/>
  <polygon points="300,53 340,53 485,303 445,303" fill="#0054AA"/>
  <g role="img" aria-label="Photo: young girl with headphones holding a phone and raising one finger">
    <rect x="132" y="0" width="195" height="303" rx="90" ry="90" fill="#b9bcc2"/>
  </g>
</svg>
<h2 class="section-title" style="left:567px;top:2722px;color:#fff;font-size:30px">OUR CLIENTS</h2>
<div class="rule" style="left:567px;top:2769px;background:#fff"></div>
<p class="body" style="left:567px;top:2791px;width:500px;color:#fff">“We’ve continued to work Martin over the years because he excels at turning ideas into viable and compelling marketing content that really reaches our target audience. His experience in the security field has also been a big plus for Vaultline, and has enabled him to add real value to our company.”</p>

<!-- WHY CHOOSE -->
<h2 class="section-title" style="left:0;width:1200px;text-align:center;top:2970px;font-size:30px">WHY CHOOSE ME</h2>
<div class="rule" style="left:584px;top:3017px"></div>
<div class="choice" style="left:208px;background:var(--orange);color:#fff">
  <h3>HIRE ME</h3>
  <ul>
    <li>Get sharp, on-brand copy that feels exquisitely right</li>
    <li>Feel confident to drive traffic to your website — because it actually reflects your value</li>
    <li>Enjoy a smoother-than-smoothie process with a personable team that delivers</li>
  </ul>
</div>
<div class="choice" style="left:600px;background:var(--grey);color:#777">
  <h3 style="text-decoration:line-through">DON’T HIRE ME</h3>
  <ul>
    <li>Lose MUCH-NEEDED income from prospects who get turned off by your (cobbled-together) brand</li>
    <li>Get flabby, yawn-inducing copy that has readers frantically flipping the page — or compulsively clicking the X button — faster than you can say “BAD INVESTMENT”</li>
    <li>Make your competitor REALLY happy</li>
  </ul>
</div>

<!-- FOOTER -->
<footer class="abs footer">
  <div class="abs" style="left:112px;top:96px;color:#fff;font-size:34px;font-weight:800;letter-spacing:1px">BRIVANE</div>
  <div class="abs" style="left:112px;top:175px;color:#fff;font-size:11px;font-weight:500;line-height:23px">COPYRIGHT © 2023 BRIVANE.<br>ALL RIGHTS RESERVED.</div>
  <h4 style="left:375px">ABOUT</h4>
  <ul style="left:375px"><li>LOREM IPSUM DOLOR SIT</li><li>AMET, CONSECTETUR</li><li>ADIPISCING ELIT, SED DO</li><li>EIUSMOD TEMPOR</li><li>INCIDIDUNT UT LABORE ET</li><li>DOLORE MAGNA ALIQUA.</li><li>QUIS IPSUM SUSPENDISSE</li></ul>
  <h4 style="left:620px">QUICK LINK</h4>
  <ul style="left:620px"><li>HOME</li><li>ABOUT</li><li>SERVICES</li><li>INDUSTRIES</li><li>PORTFOLIO</li><li>CLIENTS</li><li>CONTACT</li></ul>
  <h4 style="left:790px">FOLLOW US</h4>
  <ul style="left:790px"><li><i></i>CHATTERLY</li><li><i></i>MURMUR</li><li><i></i>SEARCHLY</li><li><i></i>LINKWELL</li></ul>
  <h4 style="left:971px">NEWSLETTER</h4>
  <div class="field" style="top:92px">NAME</div>
  <div class="field" style="top:123px">EMAIL</div>
  <div class="btn" style="left:972px;top:154px;width:100px;height:22px;font-size:10.5px">SUBMIT</div>
</footer>

</div>
</body>
</html>
```